RM Trelvano businesscard project

RM Cargoline Ltd is a freshly founded small (3 employees), young (average age is 30 years) company, living from the road transportation market without own tools.
We would like to have an impressive, new-line, cool busines card for a freshly founded forwarding company on an overcrowded market which raises attention and makes the potential partners eager to work with us.

Target Market(s)

The main profile of the company is logistic/forwarding on road.

Industry/Entity Type

Freight Forwarding

Contact Information for Business Card

Name: Berki Zsófia
Title: general manager
mobile nr: +36-70/482-5193
fax nr: +36-1/534-9061
e-mail: zsofia.berki@rmtrelvano.example
info@rmtrelvano.example
website address: http://www.rmcargoline.example
and if possible maybe some funny or helpful info on the back

Requirements
Must have
• contact details above
Nice to have
• some really nice and catching back-side (info, graphics, useful tool info... anything)
Should not have
• trucks, road, ship, airplane on it...

```html
<!DOCTYPE html>
<html lang="hu">
<head>
<meta charset="utf-8">
<title>RM Trelvano – Business Card</title>
<link href="https://fonts.googleapis.com/css2?family=Oswald:wght@400&family=Montserrat:wght@600&family=Open+Sans:wght@400&display=swap" rel="stylesheet">
<style>
  :root{
    --backdrop:#a8a6a7;
    --card:#fbfbfb;
    --brand-blue:#5f7bb0;
    --ink:#2e2e2e;
    --swoosh:#3a3a3a;
    --text-soft:#444444;
    --on-blue:#ffffff;
  }
  html,body{margin:0;padding:0;width:1200px;height:1200px;overflow:hidden;background:var(--backdrop);}
  .card{position:absolute;width:712px;height:416px;background:var(--card);border-radius:28px;overflow:hidden;}
  .card--front{left:238px;top:120px;}
  .card--back{left:231px;top:645px;}

  .brand{position:absolute;display:flex;flex-direction:column;align-items:center;gap:26px;}
  .brand__square{width:96px;height:96px;background:var(--brand-blue);}
  .brand__name{font-family:'Oswald',sans-serif;font-weight:400;color:var(--ink);line-height:1;white-space:nowrap;}
  .card--front .brand{left:0;right:0;top:92px;}
  .card--front .brand__name{font-size:52px;}
  .card--back .brand{left:70px;top:72px;gap:34px;}
  .card--back .brand__square{width:110px;height:110px;}
  .card--back .brand__name{font-size:50px;}

  .wave{position:absolute;inset:0;width:712px;height:416px;}
  .wave__fill{fill:var(--brand-blue);}
  .wave__swoosh{fill:var(--swoosh);}

  .person{position:absolute;right:57px;top:66px;text-align:right;}
  .person__name{font-family:'Montserrat',sans-serif;font-weight:600;font-size:23px;color:var(--ink);letter-spacing:.5px;}
  .person__title{font-family:'Open Sans',sans-serif;font-size:16px;color:var(--text-soft);margin-top:8px;}

  .contacts{position:absolute;right:28px;top:266px;margin:0;padding:0;list-style:none;}
  .contacts__item{display:flex;justify-content:flex-end;align-items:center;gap:12px;height:25.5px;font-family:'Open Sans',sans-serif;font-size:16.5px;color:var(--on-blue);white-space:nowrap;}
  .contacts__icon{width:16px;height:16px;fill:none;stroke:var(--on-blue);stroke-width:1.6;flex:none;}
  .contacts__icon .solid{fill:var(--on-blue);stroke:none;}
</style>
</head>
<body>

<section class="card card--front">
  <div class="brand">
    <span class="brand__square"></span>
    <span class="brand__name">RM Trelvano</span>
  </div>
</section>

<section class="card card--back">
  <svg class="wave" viewBox="0 0 712 416" aria-hidden="true">
    <path class="wave__fill" d="M0,378 C180,388 320,350 430,285 C520,232 610,198 712,190 L712,416 L0,416 Z"/>
    <path class="wave__swoosh" d="M0,318 C180,332 310,335 420,268 C515,212 605,178 712,174 L712,184 C610,190 525,222 432,278 C320,346 170,360 0,356 Z"/>
  </svg>

  <div class="brand">
    <span class="brand__square"></span>
    <span class="brand__name">RM Trelvano</span>
  </div>

  <div class="person">
    <div class="person__name">Berki Zsófia</div>
    <div class="person__title">General Manager</div>
  </div>

  <ul class="contacts">
    <li class="contacts__item">rmtrelvano.example
      <svg class="contacts__icon" viewBox="0 0 16 16"><circle cx="8" cy="8" r="6.5"/><ellipse cx="8" cy="8" rx="3" ry="6.5"/><line x1="1.5" y1="8" x2="14.5" y2="8"/></svg></li>
    <li class="contacts__item">+36-1/534-9061
      <svg class="contacts__icon" viewBox="0 0 16 16"><rect class="solid" x="1" y="6" width="14" height="6" rx="1"/><rect x="4" y="2" width="8" height="4"/><rect x="4" y="10" width="8" height="4.5"/></svg></li>
    <li class="contacts__item">+36-70/482-5193
      <svg class="contacts__icon" viewBox="0 0 16 16"><rect x="4" y="1" width="8" height="14" rx="1.5"/><circle class="solid" cx="8" cy="12.5" r="1"/></svg></li>
    <li class="contacts__item">info@rmtrelvano.example
      <svg class="contacts__icon" viewBox="0 0 16 16"><rect class="solid" x="1" y="3.5" width="14" height="9"/><polyline points="1,3.5 8,9 15,3.5" stroke="#5f7bb0"/></svg></li>
    <li class="contacts__item">zsofia.berki@rmtrelvano.example
      <svg class="contacts__icon" viewBox="0 0 16 16"><rect class="solid" x="1" y="3.5" width="14" height="9"/><polyline points="1,3.5 8,9 15,3.5" stroke="#5f7bb0"/></svg></li>
  </ul>
</section>

</body>
</html>
```